Summit Builders Web Site / Business Cards

Construction Company that specializes in Water and Fire Damage, Residential ReModels, Landscaping and Building ADU (Accessory Dwelling Unit)

Growing and changing families often need additional space, and a remodeling project can often provide that. Adding a new area, or repurposing an existing one can satisfy this requirement.

Other times, homeowners want to update the look in their kitchen or bathroom with more than just a change of cabinetry or vanity doors and drawers. Whatever your needs are, Summit Builders has skilled workers who are bonded and insured, and ready to make your dreams and visions a reality.

Target Market(s)

Home Owners

Industry/Entity Type

Construction Company

Contact Information for Business Card

Center Logo with our information on the corners

Back side to be Logo Only
Contact Info
CSLB License # 4829516
info@summitbuildersca.example
www.summitbuildersca.example

Coding

Coded - Design and coding required

Number of Pages Required

5+ page

Font styles to use
Serif
Sans Serif

Requirements
Must have
• Using our Logo Colors
Home
About Us
Services
Projects / Portfolio
Contact Us
Nice to have
• Colors matching our Logo
Should not have
• Black because it doesnt match our logo

```html
<!DOCTYPE html>
<html lang="en">
<head>
<meta charset="utf-8">
<title>Summit Builders — Business Cards</title>
<link rel="stylesheet" href="https://fonts.googleapis.com/css2?family=Red+Hat+Display:wght@500;800&display=swap">
<style>
  :root {
    --orange: #ff6a00;
    --orange-deep: #f45a05;
    --orange-light: #ff7d24;
    --white: #ffffff;
    --ink: #1c1c1c;
    --backdrop: #f3f1ee;
  }
  * { box-sizing: border-box; margin: 0; padding: 0; }
  html, body {
    width: 1200px;
    height: 814px;
    overflow: hidden;
    background: var(--backdrop);
    font-family: "Red Hat Display", sans-serif;
  }
  .sheet {
    width: 1200px;
    height: 814px;
    display: flex;
    align-items: center;
    justify-content: center;
    gap: 60px;
  }
  .card {
    width: 520px;
    height: 297px;
    border-radius: 4px;
    box-shadow: 0 14px 34px rgba(120, 60, 10, 0.18);
    position: relative;
    overflow: hidden;
  }
  .card-back {
    background: linear-gradient(135deg, var(--orange-deep), var(--orange-light));
    display: flex;
    align-items: center;
    justify-content: center;
  }
  .wordmark {
    font-weight: 800;
    font-size: 40px;
    letter-spacing: 2px;
    text-transform: uppercase;
    display: flex;
    align-items: center;
    gap: 14px;
  }
  .wordmark-mark {
    width: 18px;
    height: 18px;
    border-radius: 50%;
  }
  .card-back .wordmark { color: var(--white); }
  .card-back .wordmark-mark { background: var(--white); }

  .card-front { background: var(--white); }
  .front-brand {
    position: absolute;
    top: 0; left: 0; right: 0;
    height: 160px;
    display: flex;
    align-items: center;
    justify-content: flex-end;
    padding-right: 52px;
  }
  .card-front .wordmark { color: var(--ink); font-size: 34px; }
  .card-front .wordmark-mark { background: var(--orange); }
  .contact-band {
    position: absolute;
    left: 0; right: 0; bottom: 0;
    height: 137px;
    background: linear-gradient(135deg, var(--orange-deep), var(--orange-light));
    padding: 22px 30px;
    color: var(--white);
    font-weight: 500;
    font-size: 15px;
    display: flex;
    flex-direction: column;
    gap: 10px;
  }
  .contact-line {
    display: flex;
    align-items: center;
    gap: 10px;
  }
  .contact-line svg { width: 16px; height: 16px; flex: none; }
  .contact-line.license { padding-left: 26px; }
</style>
</head>
<body>
  <main class="sheet">
    <section class="card card-back" aria-label="Business card back">
      <div class="wordmark"><span class="wordmark-mark"></span>Summit Builders</div>
    </section>

    <section class="card card-front" aria-label="Business card front">
      <div class="front-brand">
        <div class="wordmark"><span class="wordmark-mark"></span>Summit Builders</div>
      </div>
      <div class="contact-band">
        <p class="contact-line license">CSLB License # 4829516</p>
        <p class="contact-line">
          <svg viewBox="0 0 16 16" fill="none" stroke="currentColor" stroke-width="1.2" aria-hidden="true">
            <rect x="1.5" y="3.5" width="13" height="9" rx="0.5"/>
            <path d="M1.5 3.5 8 9l6.5-5.5"/>
          </svg>
          info@summitbuildersca.example
        </p>
        <p class="contact-line">
          <svg viewBox="0 0 16 16" fill="none" stroke="currentColor" stroke-width="1.2" aria-hidden="true">
            <circle cx="8" cy="8" r="6.5"/>
            <ellipse cx="8" cy="8" rx="3" ry="6.5"/>
            <path d="M1.5 8h13M2.5 4.8h11M2.5 11.2h11"/>
          </svg>
          www.summitbuildersca.example
        </p>
      </div>
    </section>
  </main>
</body>
</html>
```